Book Cover " FROM GRAVEL TO AMBER"

Looking for a book cover for a novel from Gravel to Amber.
Amber is the characters developed name. The book describes his rough up bringing and how he obtains his greatness and his given name Amber.

```html
<!DOCTYPE html>
<html lang="en">
<head>
<meta charset="UTF-8">
<title>From Gravel to Amber — Book Cover</title>
<link href="https://fonts.googleapis.com/css2?family=Cinzel:wght@400;500&display=swap" rel="stylesheet">
<style>
  :root {
    --page: #ffffff;
    --cover-left: #0c0101;
    --cover-right: #05080a;
    --halo-ember: #6b2e2f;
    --halo-sky: #41b0e4;
    --halo-rim: #1a1f6e;
    --type: #ffffff;
  }
  * { margin: 0; padding: 0; box-sizing: border-box; }
  html, body {
    width: 1200px;
    height: 1200px;
    overflow: hidden;
    background: var(--page);
  }
  .canvas {
    position: relative;
    width: 1200px;
    height: 1200px;
  }
  .book-cover {
    position: absolute;
    left: 360px;
    top: 240px;
    width: 480px;
    height: 720px;
    overflow: hidden;
    background: linear-gradient(to right, var(--cover-left) 0 50%, var(--cover-right) 50% 100%);
  }
  .portrait-halo {
    position: absolute;
    left: 0;
    top: 0;
    width: 480px;
    height: 720px;
  }
  .subtitle {
    position: absolute;
    left: 0;
    right: 0;
    top: 46px;
    text-align: center;
    font-family: "Cinzel", serif;
    font-weight: 400;
    font-size: 27px;
    letter-spacing: 0.5px;
    color: var(--type);
    line-height: 1;
  }
  .title {
    position: absolute;
    left: 0;
    right: 0;
    top: 552px;
    text-align: center;
    font-family: "Cinzel", serif;
    font-weight: 400;
    font-size: 118px;
    letter-spacing: 2px;
    color: var(--type);
    line-height: 1;
  }
</style>
</head>
<body>
  <main class="canvas">
    <section class="book-cover">
      <svg class="portrait-halo" viewBox="0 0 480 720" role="img" aria-label="Silhouette of a young man in profile against a glowing circle, half ember red and half sky blue">
        <defs>
          <clipPath id="halo-left"><rect x="0" y="0" width="240" height="720"/></clipPath>
          <clipPath id="halo-right"><rect x="240" y="0" width="240" height="720"/></clipPath>
        </defs>
        <circle cx="241" cy="306" r="220" fill="var(--halo-rim)" clip-path="url(#halo-right)"/>
        <circle cx="241" cy="306" r="218" fill="var(--halo-ember)" clip-path="url(#halo-left)"/>
        <circle cx="241" cy="306" r="216" fill="var(--halo-sky)" clip-path="url(#halo-right)"/>
      </svg>
      <p class="subtitle">from Gravel to</p>
      <h1 class="title">AMBER</h1>
    </section>
  </main>
</body>
</html>
```